Redesign website for small print company

Vindabrot is a small printing company in Iceland mainly servicing Students, schools, etc. We are also doing all kind of other jobs, like business cards, book printing, brochure printing etc. We are also selling books online.
Our website is: www.vindabrot.is
What we are looking for is:
- Web Design (Uncoded - PSD layout only)
- Mobile friendly design, using our current color scheme: Red, green, yellow and light gray.
- Clean simple design
- Simple, light and easy to use.
- More menu Items/drop down
Industry/Entity Type
Digital Printing
Number of Pages Required
5+ page
Requirements
Must have
- Easy navigation
- Designed for mobile
- Current color scheme (see logo)
Nice to have
- Icon based products

```html
<!DOCTYPE html>
<html lang="en">
<head>
<meta charset="utf-8">
<title>Vindabrot – Shop Navigation Menu</title>
<link href="https://fonts.googleapis.com/css2?family=Poppins:wght@400;500;600;700&display=swap" rel="stylesheet">
<style>
:root{
  --red:#e8321f;
  --yellow:#ffd400;
  --ink:#33363b;
  --text:#4a4d53;
  --muted:#6c7077;
  --soft:#a3a7ad;
  --line:#ececec;
  --bubble:#efefef;
  --blue:#1a73e8;
  --page:#ffffff;
}
*{box-sizing:border-box;margin:0;padding:0}
html,body{width:1200px;height:1200px;overflow:hidden;background:var(--page)}
body{position:relative;font-family:'Poppins',sans-serif;color:var(--text)}
.panel{position:absolute;left:0;top:316px;width:1200px;height:674px;background:#fff}
.abs{position:absolute;white-space:nowrap}
.topbar{font-size:13px;color:var(--ink);top:18px}
.topbar svg{vertical-align:-1px;margin-right:6px}
.rule{position:absolute;height:1px;background:var(--line)}
.brand{position:absolute;left:524px;top:38px;display:flex;align-items:center;gap:8px}
.brand-mark{width:18px;height:18px;background:var(--red)}
.brand-name{font-size:22px;font-weight:600;color:var(--ink);letter-spacing:.2px}
.lang{left:87px;top:76px;font-size:13px;color:var(--soft);display:flex;align-items:center;gap:8px}
.tool{position:absolute;top:70px;width:35px;height:26px;border:1px solid #e4e4e4;border-radius:14px;display:flex;align-items:center;justify-content:center;background:#fff}
.badge{position:absolute;top:-6px;right:-2px;background:var(--blue);color:#fff;font-size:7px;border-radius:6px;padding:0 3px;line-height:10px}
.avatar{position:absolute;left:1088px;top:76px;width:25px;height:25px;border-radius:50%;background:var(--bubble)}
.nav a{position:absolute;top:140px;font-size:13px;color:var(--ink);text-decoration:none;font-weight:400}
.underline{position:absolute;left:296px;top:166px;width:50px;height:2px;background:var(--red)}
.gift{position:absolute;left:933px;top:140px;width:92px;height:20px;border-radius:10px;background:var(--yellow);color:#fff;font-size:12.5px;font-weight:500;text-align:center;line-height:20px}
.find{left:1038px;top:140px;font-size:13px;color:var(--soft)}
.col{position:absolute;top:203px}
.col h3{font-size:17.5px;font-weight:700;color:var(--muted);letter-spacing:.4px;margin-bottom:24px}
.col li{list-style:none;font-size:12.5px;color:var(--ink);height:30.7px}
.promo{position:absolute;left:87px;top:384px}
.promo-title{font-size:12.5px;font-weight:600;color:var(--text)}
.promo-image{width:78px;height:78px;margin-top:10px;background:linear-gradient(135deg,#d9d7d3,#f3f2ef 55%,#e6e4e0)}
.promo-name{font-size:12.5px;font-weight:600;color:var(--text);margin-top:14px}
.promo-sale{font-size:12.5px;color:var(--red);margin-top:10px}
.all{position:absolute;top:597px;font-size:12.5px;font-weight:600;color:var(--muted);white-space:nowrap}
</style>
</head>
<body>

<header class="panel">
  <div class="abs topbar" style="left:87px">
    <svg width="10" height="10" viewBox="0 0 10 10"><path d="M2 0.5 L3.6 2.6 L2.8 3.6 C3.4 5 4.8 6.4 6.2 7.1 L7.3 6.2 L9.5 7.8 L8.4 9.5 C4.5 9.2 0.8 5.5 0.5 1.6Z" fill="var(--ink)"/></svg>555 0142
    <span style="margin-left:16px"><svg width="11" height="8" viewBox="0 0 11 8"><rect width="11" height="8" rx="1" fill="var(--ink)"/><path d="M0.5 0.8 L5.5 4.5 L10.5 0.8" stroke="#fff" fill="none" stroke-width="1"/></svg>verk@vindabrot.is</span>
  </div>
  <div class="abs topbar" style="left:1004px">
    <svg width="10" height="10" viewBox="0 0 10 10"><circle cx="5" cy="5" r="4.3" fill="none" stroke="var(--ink)" stroke-width="1"/><path d="M5 2.5 V5 H7" fill="none" stroke="var(--ink)" stroke-width="1"/></svg>Mon - Fri: 9-17
  </div>
  <div class="rule" style="left:0;top:50px;width:1200px"></div>

  <div class="brand"><span class="brand-mark"></span><span class="brand-name">VINDABROT</span></div>

  <div class="abs lang">
    <svg width="15" height="15" viewBox="0 0 15 15"><circle cx="7.5" cy="7.5" r="7.5" fill="#2a4a9c"/><path d="M0 7.5H15M7.5 0V15" stroke="#fff" stroke-width="3"/><path d="M0 7.5H15M7.5 0V15" stroke="var(--red)" stroke-width="1.5"/></svg>
    English - UK
    <svg width="8" height="5" viewBox="0 0 8 5"><path d="M1 1 L4 4 L7 1" fill="none" stroke="var(--soft)" stroke-width="1"/></svg>
  </div>

  <div class="tool" style="left:998px">
    <svg width="11" height="11" viewBox="0 0 11 11"><circle cx="4.8" cy="4.8" r="3.8" fill="none" stroke="var(--ink)" stroke-width="1.2"/><path d="M7.6 7.6 L10 10" stroke="var(--ink)" stroke-width="1.2"/></svg>
  </div>
  <div class="tool" style="left:1043px">
    <svg width="12" height="11" viewBox="0 0 12 11"><path d="M0.5 1 H2.5 L4 7 H10 L11.2 2.5 H3" fill="none" stroke="var(--ink)" stroke-width="1.1"/><circle cx="4.8" cy="9.3" r=".9" fill="var(--ink)"/><circle cx="9.2" cy="9.3" r=".9" fill="var(--ink)"/></svg>
    <span class="badge">47</span>
  </div>
  <div class="avatar"></div>

  <div class="rule" style="left:19px;top:125px;width:1162px;background:#e4e4e4"></div>

  <nav class="nav">
    <a style="left:105px">Home</a>
    <a style="left:190px">Popular <svg width="8" height="5" viewBox="0 0 8 5" style="margin-left:5px"><path d="M1 1 L4 4 L7 1" fill="none" stroke="var(--ink)" stroke-width="1.2"/></svg></a>
    <a style="left:296px">Shop <svg width="8" height="5" viewBox="0 0 8 5" style="margin-left:5px"><path d="M1 4 L4 1 L7 4" fill="none" stroke="var(--ink)" stroke-width="1.2"/></svg></a>
    <a style="left:378px">Job Submit</a>
    <a style="left:487px">About Us</a>
  </nav>
  <div class="underline"></div>
  <div class="gift">Gift Cards</div>
  <div class="abs find">Find a store</div>
  <div class="rule" style="left:0;top:168px;width:1200px;background:#f4f4f4"></div>

  <div class="col" style="left:87px"><h3>ART PRINTS</h3><ul><li>A3 Size</li><li>A4 Size</li><li>A5 Size</li><li>--</li></ul></div>
  <div class="col" style="left:250px"><h3>FLYERS</h3><ul><li>A4 Size</li><li>A5 Size</li><li>A6 Size</li><li>A7 Size</li></ul></div>
  <div class="col" style="left:370px"><h3>INVITATIONS</h3><ul><li>A5 Size</li><li>A6 Size</li></ul></div>
  <div class="col" style="left:545px"><h3>MENUS</h3><ul><li>A5 Size</li><li>A6 Size</li></ul></div>
  <div class="col" style="left:666px"><h3>POSTCARDS</h3><ul><li>A4 Size</li><li>A5 Size</li><li>A6 Size</li><li>A7 Size</li></ul></div>
  <div class="col" style="left:833px"><h3>POSTERS</h3><ul><li>A3 Size</li><li>A4 Size</li></ul></div>

  <div class="promo">
    <div class="promo-title">Holiday is coming</div>
    <div class="promo-image" role="img" aria-label="Photo of a Christmas card with a red bauble standing in a bright room"></div>
    <div class="promo-name">Christmas Cards</div>
    <div class="promo-sale">Flash sale 50% off</div>
  </div>

  <div class="rule" style="left:19px;top:583px;width:1162px;background:#e4e4e4"></div>
  <div class="all" style="left:87px">All Art Print's ›</div>
  <div class="all" style="left:250px">All Flyer's ›</div>
  <div class="all" style="left:370px">All Invitation's ›</div>
  <div class="all" style="left:545px">All Menu's ›</div>
  <div class="all" style="left:666px">All Postcard's ›</div>
  <div class="all" style="left:833px">All Poster's ›</div>
</header>

</body>
</html>
```